Modern Retail Coffee Label for established Roastery! 17 years!

We are looking for a Retail Coffee Bag Label... JUST THE LABEL TO GO ON AN EXISTING BAG. Our current label is provided and our Logo.. we have had the same Red Bags FOREVER so we are looking for a label to compliment that tradition and to be placed on the bags we have used for 17 years.

We have a retail line of bags with locally roasted coffee. Our business has been around 17years and is in need of a design upgrade! We have a red coffee bag and are looking for a sleek modern label. I will attach a file of our label right now so you can see what it looks like. We are just looking for a more modern version. a few inclusions:

Locally Roasted
100% Arabica Coffee
Heron Kin's Coffee
heronkincoffee.example
logo

The black label with the red and yellow color label is the old one... the new label should be the White background and black border one...

Target Market(s)

Retail Coffee Consumers

Font styles to use
Other font styles liked:
• use what you think. we are located in SW Wisconsin but ship coffee EVERYWHERE

Colors

Designer to choose only greyscale colors for use in the design.

Requirements
Must have
• Locally Roasted (Platteville,WI)
• 100% Arabica Coffee
• heronkincoffee.example
• logo
Nice to have
• Badgers
• "Since 2003"
Should not have
• Any lunabrew or big brand themes

```html
<!DOCTYPE html>
<html lang="en">
<head>
<meta charset="utf-8">
<title>Heron Kin's Coffee — Retail Bag Label</title>
<link rel="stylesheet" href="https://fonts.googleapis.com/css2?family=Quattrocento+Sans:wght@400;700&family=Lato:wght@400;700&display=swap">
<style>
  :root {
    --paper: #ffffff;
    --ink: #111111;
    --frame-thin: #1a1a1a;
  }
  * { margin: 0; padding: 0; box-sizing: border-box; }
  html, body {
    width: 771px;
    height: 1200px;
    overflow: hidden;
    background: var(--paper);
  }
  .label {
    position: relative;
    width: 771px;
    height: 1200px;
    background: var(--paper);
    color: var(--ink);
    font-family: "Quattrocento Sans", sans-serif;
  }
  .outer-frame {
    position: absolute;
    left: 39px; top: 33px;
    width: 694px; height: 1133px;
    border: 2px solid var(--frame-thin);
  }
  .inner-frame {
    position: absolute;
    left: 101px; top: 75px;
    width: 574px; height: 963px;
    border: 7px solid var(--ink);
  }
  .centered {
    position: absolute;
    left: 0; width: 771px;
    text-align: center;
    line-height: 1;
  }
  .brand-name {
    top: 180px;
    font-weight: 700;
    font-size: 54px;
    letter-spacing: 0.04em;
    line-height: 1.35;
    text-transform: uppercase;
  }
  .since {
    top: 402px;
    font-size: 40px;
    letter-spacing: 0.3em;
    padding-left: 0.3em;
  }
  .rule {
    position: absolute;
    left: 137px;
    width: 497px;
    height: 4px;
    background: var(--ink);
  }
  .rule-top { top: 469px; }
  .rule-bottom { top: 784px; }
  .percent {
    top: 505px;
    font-size: 104px;
    font-weight: 400;
    letter-spacing: 0.06em;
    padding-left: 0.06em;
  }
  .bean-type {
    top: 608px;
    font-size: 80px;
    font-weight: 700;
    letter-spacing: 0.22em;
    padding-left: 0.22em;
  }
  .product {
    top: 696px;
    font-size: 62px;
    font-weight: 400;
    letter-spacing: 0.3em;
    padding-left: 0.3em;
  }
  .roast-claim {
    top: 908px;
    font-family: "Lato", sans-serif;
    font-size: 57px;
    font-weight: 400;
    letter-spacing: -0.01em;
  }
  .roast-town {
    top: 975px;
    font-family: "Lato", sans-serif;
    font-size: 37px;
  }
  .web-address {
    top: 1085px;
    font-family: "Lato", sans-serif;
    font-size: 31px;
    letter-spacing: 0.01em;
  }
</style>
</head>
<body>
  <main class="label">
    <div class="outer-frame"></div>
    <div class="inner-frame"></div>

    <h1 class="centered brand-name">Heron Kin's<br>Coffee</h1>
    <p class="centered since">SINCE 2003</p>

    <div class="rule rule-top"></div>
    <p class="centered percent">100%</p>
    <p class="centered bean-type">ARABICA</p>
    <p class="centered product">COFFEE</p>
    <div class="rule rule-bottom"></div>

    <p class="centered roast-claim">LOCALLY ROASTED</p>
    <p class="centered roast-town">(Platteville, WI)</p>

    <p class="centered web-address">www.heronkincoffee.example</p>
  </main>
</body>
</html>
```